AMAZING WEBSITE DESIGN NEEDED FOR MAID / CLEANING SERVICE

NOTE: This is Website Design Only - No coding required

Please submit your designs ASAP as we want to pick a winner and get started!

Hey,

We are looking for a new amazing website design for a maid or cleaning service.

They have a horrible website that we want turned into a masterpiece.

As you will see on their current site:

http://tidyharborco.examplehost.net/

They have a lot of stuff, very disorganized, and need help.

Here is what we need:

Colors: Same as current site, Orange, Gray, Black

Menu: Horizontal with same Menu items

Need a spot for a video on the homepage

Want content to be structured in a great format that is easy to read.

Want to highlight commercial and residential on the website homepage.

Also want a spot for customer testimonials

We want the site clean, professional, fresh and modern.

Please help by matching the logo design.

I look forward to your designs!
Updates

Hi All! Really appreciate your efforts and designs. I will be meeting with our client on Monday and will then be able to provide feedback after our meeting. If you have other ideas, please submit them. The more I can show him the better! Thanks!

Target Market(s)

The target market is residential home owners as well as commercial businesses who need cleaning on a regular basis.

This company cleans homes and offices for individuals.

Industry/Entity Type

Residential

Font styles to use
Sans Serif

Requirements
Must have
• Must match logo colors
Must have spot for video
Must have a clean look
Must have a bold look
Nice to have
• Highly visual
Should not have
• clutter
messy design
hard to read

```html
<!DOCTYPE html>
<html lang="en">
<head>
<meta charset="utf-8">
<title>Tidy Harbor — Home</title>
<link href="https://fonts.googleapis.com/css2?family=Open+Sans:wght@400;600;700;800&display=swap" rel="stylesheet">
<style>
:root{
  --orange:#f07d1f;
  --orange-dark:#d96a10;
  --nav:#3c3c3c;
  --dark:#2a2a2a;
  --gray:#8a8a8a;
  --light:#eeeeee;
  --footer:#e6e6e6;
  --text:#444;
  --white:#fff;
}
*{box-sizing:border-box;margin:0;padding:0}
html,body{width:1200px;height:3600px;overflow:hidden}
body{font-family:"Open Sans",Arial,sans-serif;color:var(--text);background:var(--white);position:relative}
.abs{position:absolute}
/* header */
.site-header{top:0;left:0;width:1200px;height:93px}
.brand{left:48px;top:18px;display:flex;align-items:center;gap:10px}
.brand-mark{width:40px;height:40px;background:var(--orange)}
.brand-name{font-weight:800;font-size:30px;color:var(--dark);letter-spacing:.5px}
.brand-tag{left:100px;top:60px;font-size:10px;color:var(--gray)}
.contact{top:20px;left:780px;font-size:12px;line-height:17px;color:var(--text)}
.contact-right{left:1010px}
/* nav */
.main-nav{top:93px;left:0;width:1200px;height:30px;background:var(--nav);display:flex;flex-wrap:nowrap;padding-left:45px;overflow:hidden}
.main-nav a{flex:none;white-space:nowrap;color:var(--white);font-size:10px;font-weight:700;text-decoration:none;text-transform:uppercase;padding:0 11px;line-height:30px;border-right:1px solid #555}
.main-nav a.active{background:var(--orange)}
/* hero */
.hero{top:123px;left:0;width:1200px;height:450px;background:linear-gradient(135deg,#d8d8d8 0%,#f4f4f4 35%,#bdbdbd 60%,#2a2a2a 100%)}
.hero-title{left:375px;top:170px;font-size:94px;line-height:92px;font-weight:800;color:var(--white);text-transform:uppercase;letter-spacing:2px;text-shadow:0 2px 6px rgba(0,0,0,.25);white-space:nowrap}
.hero-arrow{top:290px;width:30px;height:30px;border-radius:50%;background:rgba(120,120,120,.7)}
/* section headings */
.section-title{left:0;width:1200px;text-align:center;font-size:14px;color:var(--text)}
.section-title span{background:var(--white);padding:0 18px;position:relative}
.section-title::before{content:"";position:absolute;left:420px;right:420px;top:50%;border-top:1px solid #ccc}
/* about */
.about{top:690px;left:0;width:1200px;height:375px;background:var(--orange);color:var(--white);text-align:center;padding:40px 90px;font-size:12.5px;line-height:19px}
.about p{margin-bottom:14px}
/* video */
.video{top:1170px;left:45px;width:810px;height:450px;background:linear-gradient(180deg,#1d2b3a 0%,#2d4660 55%,#0f1620 100%)}
.video-meta{left:18px;top:14px;display:flex;gap:10px;align-items:center}
.video-thumb{width:44px;height:44px;background:#6b7f95}
.video-title{color:#3aa7e0;font-size:22px;font-weight:700;line-height:24px}
.video-by{color:var(--white);font-size:13px}
.video-by b{color:#3aa7e0}
.video-buy{right:70px;top:20px;background:rgba(0,0,0,.7);color:var(--white);font-size:15px;font-weight:700;padding:8px 14px}
.video-tools{right:14px;top:16px;display:flex;flex-direction:column;gap:10px}
.video-tools i{display:block;width:40px;height:40px;border-radius:50%;background:rgba(0,0,0,.7)}
.video-bar{left:14px;bottom:14px;width:782px;height:38px;background:rgba(0,0,0,.7);display:flex;align-items:center;gap:12px;padding:0 12px}
.video-track{flex:1;height:8px;background:#555}
.video-track i{display:block;width:4%;height:8px;background:#3aa7e0}
.video-time{background:#3aa7e0;color:var(--white);font-size:11px;padding:2px 5px}
.share{left:888px;top:1490px;display:flex;gap:8px}
.share i{display:block;height:18px;background:#ddd;border-radius:3px;font-style:normal;font-size:10px;line-height:18px;padding:0 8px;color:#333;white-space:nowrap}
.video-side-title{left:888px;top:1518px;font-size:26px;font-weight:700;color:var(--dark);white-space:nowrap}
/* services */
.photo{background:linear-gradient(160deg,#cfd6da,#8a96a0)}
.card{background:var(--orange);color:var(--white);padding:24px 22px}
.card h3{font-size:14px;font-weight:700;margin:10px 0 8px}
.card p{font-size:10.5px;line-height:15px}
.card-shop{top:1740px;left:870px;width:285px;height:300px;text-align:center}
.card-home{top:2145px;left:45px;width:255px;height:375px}
/* why */
.why{top:2625px;left:0;width:1200px;height:435px;background:linear-gradient(180deg,#3a3a3a,#1e1e1e);display:flex;justify-content:center;gap:70px;padding-top:115px}
.why-item{width:175px;text-align:center;color:var(--white);font-size:11.5px;line-height:16px;font-weight:600}
.why-item svg{display:block;margin:0 auto 22px}
/* testimonials */
.testimonials{top:3130px;left:45px;width:1110px;display:flex;gap:45px}
.quote{flex:1;display:flex;gap:16px}
.avatar{width:100px;height:100px;border-radius:50%;background:linear-gradient(180deg,#b9a99a,#6f6358);flex:none}
.quote p{font-size:10.5px;line-height:15px;color:#555}
.quote cite{display:block;color:var(--orange);font-style:normal;margin-top:4px}
/* footer */
.site-footer{top:3285px;left:0;width:1200px;height:285px;background:var(--footer)}
.footer-links{left:57px;top:25px;list-style:none;font-size:11px;line-height:22px;text-transform:uppercase;color:#444}
.footer-social{left:336px;top:25px;font-size:11px;color:#444}
.footer-social i{display:inline-block;width:48px;height:16px;background:#c8c8c8;border-radius:3px;margin-top:8px}
.footer-contact{left:650px;top:25px;font-size:11px;line-height:22px;color:#444}
.footer-brand{left:985px;top:30px;display:flex;align-items:center;gap:8px}
.footer-brand i{width:28px;height:28px;background:#888}
.footer-brand b{font-size:20px;font-weight:800;color:#555}
.copyright{top:3570px;left:0;width:1200px;height:30px;background:#d6d6d6;text-align:right;padding-right:60px;font-size:10px;line-height:30px;color:#666}
</style>
</head>
<body>

<header class="site-header abs">
  <div class="brand abs"><span class="brand-mark"></span><span class="brand-name">Tidy Harbor</span></div>
  <div class="brand-tag abs">Quality Commercial &amp; Residential Cleaning</div>
  <div class="contact abs">Tidy Harbor LLC<br>4120 Lantern Ridge Road NE Suite 310<br>Cedar Falls | Iowa | 50613</div>
  <div class="contact contact-right abs">(555) 014-2286 Office<br>(555) 014-2290 Fax<br>hello@tidyharbor.example</div>
</header>

<nav class="main-nav abs">
  <a class="active" href="#">Home</a><a href="#">Our Service</a><a href="#">Our Employees</a><a href="#">Why Choose Tidy Harbor?</a><a href="#">What Our Customers Are Saying?</a><a href="#">Special Offers</a><a href="#">About Us</a><a href="#">Contact Us</a><a href="#">Request a Bid</a><a href="#">Meet the President &amp; CEO</a>
</nav>

<section class="hero abs" role="img" aria-label="Photo of a bright modern living room with a white sofa and red accents">
  <h1 class="hero-title abs">Perfectly<br>clean house &amp;<br>office.</h1>
  <span class="hero-arrow abs" style="left:15px"></span>
  <span class="hero-arrow abs" style="right:15px"></span>
</section>

<h2 class="section-title abs" style="top:622px"><span>Who we are?</span></h2>

<section class="about abs">
  <p>Our team delivers dependable, professional cleaning for homes and offices across the region. We treat every space as if it were our own, arriving on time, working carefully and leaving rooms fresh, bright and ready to enjoy. Whether you need a weekly visit or a single deep clean, our crews follow a clear checklist so nothing gets missed, and our friendly office staff keeps scheduling simple.</p>
  <p>Locally Owned &amp; Operated<br>Never deal with an unresponsive franchise – deal with the owner!</p>
  <p>We are a family business built on trust. Every cleaner is screened, trained and insured, and we stand behind every job with a satisfaction promise. If something is not right, call us and we will come back to fix it quickly at no extra cost.</p>
  <p>Residential · Commercial · Office Buildings · Car Dealerships · Party Set-up &amp; Clean-up · Parking Lot Cleaning · RVs · Warehouses ... we do it ALL!</p>
  <p>First impressions are everything! We will make you or break you. Show your clients a sparkling clean office building, a professional staff and an enjoyable comfortable waiting area for your clients to love!</p>
  <p>Your Unlimited service for one true price! There are never any hidden fees, overages or sneaky charges. The price is the price! Honesty and integrity is who we are! That's the Tidy Harbor way!</p>
</section>

<section class="video abs" role="img" aria-label="Video player showing a dusky road scene as the still frame">
  <div class="video-meta abs"><span class="video-thumb"></span><div><div class="video-title">Hollow Creek</div><div class="video-by">from <b>Lena Marsh</b></div></div></div>
  <div class="video-buy abs">Purchase from $3.99</div>
  <div class="video-tools abs"><i></i><i></i><i></i><i></i></div>
  <div class="video-bar abs">
    <svg width="14" height="16" viewBox="0 0 14 16"><path d="M0 0L14 8L0 16Z" fill="#fff"/></svg>
    <div class="video-track"><i></i></div>
    <span class="video-time">03:53</span>
  </div>
</section>
<div class="share abs"><i>Share 3.9K</i><i>Like 184</i><i>Share 15</i></div>
<div class="video-side-title abs">Tidy Harbor</div>

<h2 class="section-title abs" style="top:1676px"><span>What we do?</span></h2>

<div class="photo abs" style="top:1740px;left:45px;width:804px;height:375px" role="img" aria-label="Photo of a cleaner mopping a hallway floor"></div>
<article class="card card-shop abs">
  <svg width="60" height="52" viewBox="0 0 60 52"><rect x="2" y="2" width="56" height="12" fill="#fff"/><rect x="6" y="16" width="48" height="34" fill="none" stroke="#fff" stroke-width="4"/><rect x="24" y="30" width="12" height="20" fill="#fff"/></svg>
  <h3>Commercial &amp; Office</h3>
  <p>A clean workplace lifts morale and impresses every visitor. Our crews work after hours or on your schedule, handling lobbies, break rooms, restrooms and offices with care. We follow a detailed plan for every site, so your team walks into a fresh, tidy space each morning without lifting a finger.</p>
</article>

<article class="card card-home abs">
  <svg width="46" height="42" viewBox="0 0 46 42"><path d="M23 2L2 20h6v20h30V20h6Z" fill="#fff"/><rect x="19" y="26" width="8" height="14" fill="#f07d1f"/></svg>
  <h3>Residential</h3>
  <p>Come home to a spotless house. Our trusted cleaners dust, vacuum, scrub kitchens and bathrooms, and leave every room smelling fresh. Choose weekly, biweekly or monthly service, and we will tailor each visit to your home and family so you can spend more time doing the things you love.</p>
</article>
<div class="photo abs" style="top:2145px;left:321px;width:834px;height:375px;background:linear-gradient(160deg,#e8d3b0,#a7743f)" role="img" aria-label="Photo of two cleaners dusting kitchen cabinets"></div>

<h2 class="section-title abs" style="top:2570px"><span>Why choose us?</span></h2>

<section class="why abs" role="img" aria-label="Dark background photo of cleaning gloves and supplies">
  <div class="why-item"><svg width="70" height="70" viewBox="0 0 70 70"><path d="M10 60C10 25 35 8 62 8C62 40 42 60 10 60Z" fill="#fff"/></svg>Tidy Harbor is committed to using Eco-friendly chemicals to keep you and your family safe.</div>
  <div class="why-item"><svg width="70" height="70" viewBox="0 0 70 70"><path d="M35 6L4 32h9v30h44V32h9Z" fill="#fff"/></svg>Proudly serving our amazing customers in the Cedar Falls area &amp; surrounding areas.</div>
  <div class="why-item"><svg width="70" height="70" viewBox="0 0 70 70"><rect x="28" y="8" width="14" height="54" fill="#fff"/><rect x="8" y="28" width="54" height="14" fill="#fff"/></svg>Tidy Harbor proudly donates a share of its earnings to help local families in need.</div>
  <div class="why-item"><svg width="70" height="70" viewBox="0 0 70 70"><circle cx="35" cy="35" r="30" fill="#fff"/></svg>We guarantee you will be 100% satisfied with our cleaning and our cleaning professionals!</div>
</section>

<h2 class="section-title abs" style="top:3080px"><span>What our customers are saying?</span></h2>

<section class="testimonials abs">
  <div class="quote"><div class="avatar" role="img" aria-label="Customer portrait"></div><p>“I was very impressed with the crew. They arrived on time and worked hard all day. Our house has never looked better and I would recommend them to everyone.”<cite>— Read More</cite></p></div>
  <div class="quote"><div class="avatar" role="img" aria-label="Customer portrait"></div><p>“Thank you for the wonderful cleaning. Every room sparkled and the team was polite and careful with our things. We booked them again right away.”<cite>— Read More</cite></p></div>
  <div class="quote"><div class="avatar" role="img" aria-label="Customer portrait"></div><p>“I was very happy with the cleaning. The staff was friendly, the price was fair and our office looked fresh when we walked in Monday morning.”<cite>— Read More</cite></p></div>
</section>

<footer class="site-footer abs">
  <ul class="footer-links abs"><li>Our Service</li><li>Our Employees</li><li>Why Choose Tidy Harbor?</li><li>What Our Customers Are Saying</li><li>Special Offers</li><li>About Us</li><li>Contact Us</li><li>Request a Bid</li><li>Meet the President &amp; CEO</li></ul>
  <div class="footer-social abs">Connect with us:<br><i></i><br><i></i></div>
  <div class="footer-contact abs">Tidy Harbor<br>4120 Lantern Ridge Road NE Suite 310<br>Cedar Falls | Iowa | 50613<br>(555) 014-2286 Office<br>(555) 014-2290 Fax<br>hello@tidyharbor.example</div>
  <div class="footer-brand abs"><i></i><b>Tidy Harbor</b></div>
</footer>
<div class="copyright abs">© Copyright 2014 Tidy Harbor LLC. All rights reserved.</div>

</body>
</html>
```